Velmora, Inc. Website

Looking for a website design and build for Velmora, Inc. an intellectual property incubator for the recreational and medical cannabis space in California. Our logo and brand identity has been completed website so w can begin our SEO leg of brand development.

See more details in Must haves and Nice to Haves

Target Market(s)

Target market

Vision

Our proprietary ideas have been developed to shift the approach on how whole body wellness and healing is achieved. Velmora's patent pending designs and formulations are rooted in the desire to find the most efficient, customizable, and convenient  method to precisely micro-despense whole plant cannabis extracts. 

Our ideas, designs and development team are supported by leading chemists specializing in cannabis extraction technology, leading medical doctors collaborating to develop our proprietary cannabis formulations and a passion to shift landscape of healing from a dependency on isolated symptom treatment to whole body, whole plant, whole life wellness for ourselves and our families. 

Goal

Develop, patent, and trademark our proprietary devices, formulations, and ideas for the purpose of licensing, manufacturing and distributing in the Cannabis Industry.

Industry/Entity Type

Medical

Coding

Coded - Design and coding required

Number of Pages Required

5+ page

Font styles to use
Other font styles liked:
• See Brand Identity Guide

Requirements
Must have
• Look and Feel: We are developing products, intellectual property and platforms to bring together the medical, health & wellness, and cannabis industries to provide individuals and families alike a innovative solutions to chronic illness, mood disorders, and over all wellbeing.
• Page Titles
• Home - Landing Page
• Vision-
• IP Technology & Products - will remain under construction
• Team
• Strategic Partners – will remain under construction
• Invest- will need a form to aquire contact information as well as have some questions that need to be answered to help evaluate to the potential interested party
• Contact Us– Velmora address and info@ email
Nice to have
• Images - wellness, balance, health, healing, herbs, not just cannabis, aromatherapy, mediation, energy work, dna, scientific research, microdosing, medical testing
• Style sleek and innovative - cutting edge technology - inspire to learn more
• For Colors and Fonts - See Brand Identity Guide
• Site layouts that we like are:
• http://www.thepravexgroup.example
• https://www.duneloftcare.example
• https://www.sorvanti.example
• https://www.quolt.example
• https://www.tarefy.example
Should not have
• Should not have to many cannabis images - imagery should balanced between cannabis, medical & recreational, health and wellness, mental health

```html
<!DOCTYPE html>
<html lang="en">
<head>
<meta charset="utf-8">
<title>Velmora, Inc.</title>
<link href="https://fonts.googleapis.com/css2?family=Jost:wght@400;500;600&display=swap" rel="stylesheet">
<style>
:root{
  --purple:#8b4a9c;
  --purple-deep:#4a1a4e;
  --green-deep:#0b6b3a;
  --green:#3cb34a;
  --ink:#3b3b3b;
  --text:#555;
  --white:#fff;
  --ring:#e4e4e4;
}
*{margin:0;padding:0;box-sizing:border-box}
html,body{width:1200px;height:1200px;overflow:hidden;background:#fff;font-family:"Jost",sans-serif}
.page{position:relative;width:1200px;height:1200px;overflow:hidden}
.hero{position:absolute;left:0;top:0;width:1200px;height:555px;
  background:radial-gradient(ellipse at 70% 40%,#6f8a4a 0%,#3e5a2c 45%,#1f3418 100%)}
.hero-path{position:absolute;left:0;top:0;width:1200px;height:555px;
  background:linear-gradient(170deg,transparent 55%,rgba(180,175,160,.45) 75%,rgba(90,120,50,.5) 100%)}
.brand{position:absolute;left:107px;top:10px;display:flex;align-items:center;gap:10px;color:var(--white);font-weight:500;font-size:18px;letter-spacing:2px}
.brand-mark{width:30px;height:30px;border:2px solid var(--white);border-radius:50%}
.nav{position:absolute;top:38px;left:0;width:1200px;height:24px}
.nav a{position:absolute;color:var(--white);text-decoration:none;font-size:14.5px;letter-spacing:-.3px}
.nav a.active::after{content:"";position:absolute;left:-5px;right:-5px;bottom:-6px;height:1px;background:#c58fd6}
.search{position:absolute;left:1061px;top:34px;width:32px;height:32px;border-radius:50%;background:rgba(40,40,40,.55)}
.hero-title{position:absolute;left:106px;top:225px;color:var(--white);font-size:66px;font-weight:400;letter-spacing:-3.5px}
.hero-lead{position:absolute;left:108px;top:320px;width:520px;color:var(--white);font-size:16px;line-height:26px;letter-spacing:-.6px}
.btn{position:absolute;left:108px;top:423px;width:160px;height:38px;border-radius:19px;border:1px solid #d6b5e0;
  background:linear-gradient(#b070c4,#6c2a82);color:var(--white);font-size:16px;letter-spacing:-.5px;display:flex;align-items:center;justify-content:center}
.section-title{position:absolute;left:0;top:622px;width:1200px;text-align:center;font-size:32px;color:var(--ink);font-weight:400}
.rule{position:absolute;top:647px;height:1px;width:80px;background:#cfd8cf}
.dot{position:absolute;top:643px;width:7px;height:7px;background:#9fd3a8;transform:rotate(45deg)}
.diagram{position:absolute;left:0;top:0}
.service{position:absolute;left:600px;width:500px}
.icon{position:absolute;left:0;width:88px;height:88px;border-radius:50%;border:3px solid var(--ring);background:#fff;box-shadow:0 6px 6px -4px rgba(0,0,0,.15)}
.service h3{position:absolute;left:119px;top:-6px;font-weight:400;font-size:15px;color:var(--ink);letter-spacing:.3px}
.service p{position:absolute;left:119px;top:18px;width:380px;font-size:11.6px;line-height:18.5px;color:var(--text);letter-spacing:.3px}
.about-photo{position:absolute;top:1138px;height:62px;background:linear-gradient(#e8e6dc,#8c9a62)}
.about-panel{position:absolute;left:303px;top:1107px;width:595px;height:93px;background:var(--purple)}
.about-bracket{position:absolute;left:23px;top:57px;width:34px;height:40px;border-left:1px solid #fff;border-top:1px solid #fff}
.about-title{position:absolute;left:57px;top:64px;color:#fff;font-size:29px;font-weight:400}
.about-person{position:absolute;left:347px;top:57px;width:189px;height:40px;background:linear-gradient(#c8d4d0,#9aa7a3)}
</style>
</head>
<body>
<div class="page">
  <div class="hero" role="img" aria-label="Photo of a smiling couple jogging on a park path among trees"></div>
  <div class="hero-path"></div>
  <div class="brand"><span class="brand-mark"></span>VELMORA</div>
  <nav class="nav">
    <a class="active" style="left:534px">Home</a>
    <a style="left:620px">Services</a>
    <a style="left:719px">About us</a>
    <a style="left:823px">Why Velmora</a>
    <a style="left:956px">Contact us</a>
  </nav>
  <div class="search">
    <svg width="32" height="32" viewBox="0 0 32 32"><circle cx="15" cy="15" r="5" fill="none" stroke="#fff" stroke-width="2"/><line x1="19" y1="19" x2="22" y2="22" stroke="#fff" stroke-width="2.5" stroke-linecap="round"/></svg>
  </div>
  <h1 class="hero-title">Welcome to velmora</h1>
  <p class="hero-lead">An intellectual property incubator for the recreational and medical cannabis space in California The first business incubator for brands that are changing the land-scape of&nbsp; and cannabis consumption technologies.</p>
  <div class="btn">Read More</div>

  <div class="rule" style="left:396px"></div>
  <div class="dot" style="left:484px"></div>
  <h2 class="section-title">Our Services</h2>
  <div class="dot" style="left:710px"></div>
  <div class="rule" style="left:725px"></div>

  <svg class="diagram" width="1200" height="1200" viewBox="0 0 1200 1200">
    <defs>
      <clipPath id="d-shape"><path d="M107 750 H330 A125 125 0 0 1 330 1000 H107 Z"/></clipPath>
    </defs>
    <g clip-path="url(#d-shape)">
      <rect x="107" y="750" width="360" height="57" fill="#8b4a9c"/>
      <rect x="107" y="814" width="360" height="57" fill="#0b6b3a"/>
      <rect x="107" y="878" width="360" height="58" fill="#4a1a4e"/>
      <rect x="107" y="942" width="360" height="58" fill="#3cb34a"/>
    </g>
    <circle cx="418" cy="874" r="73" fill="#e4e4e4"/>
    <circle cx="418" cy="874" r="62" fill="#fff"/>
    <text x="418" y="882" text-anchor="middle" font-family="Jost,sans-serif" font-weight="600" font-size="19" fill="#4a1a4e">VELMORA</text>
    <g font-family="Jost,sans-serif" fill="#fff">
      <text x="122" y="766" font-size="13" letter-spacing=".5">Lorem ipsum dolor sit</text>
      <text x="133" y="783" font-size="9">•&#160; Lorem ipsum dolor</text>
      <text x="133" y="797" font-size="9">•&#160; Lorem ipsum dolor</text>
      <text x="122" y="832" font-size="13" letter-spacing=".5">Lorem ipsum dolor sit</text>
      <text x="133" y="849" font-size="9">•&#160; Lorem ipsum dolor</text>
      <text x="133" y="863" font-size="9">•&#160; Lorem ipsum dolor</text>
      <text x="122" y="895" font-size="13" letter-spacing=".5">Lorem ipsum dolor sit</text>
      <text x="133" y="912" font-size="9">•&#160; Lorem ipsum dolor</text>
      <text x="133" y="926" font-size="9">•&#160; Lorem ipsum dolor</text>
      <text x="122" y="959" font-size="13" letter-spacing=".5">Lorem ipsum dolor sit</text>
      <text x="133" y="976" font-size="9">•&#160; Lorem ipsum dolor</text>
      <text x="133" y="990" font-size="9">•&#160; Lorem ipsum dolor</text>
    </g>
  </svg>

  <div class="service" style="top:735px">
    <div class="icon" style="top:-22px">
      <svg width="82" height="82" viewBox="0 0 82 82"><rect x="24" y="24" width="34" height="34" rx="9" fill="none" stroke="#8b4a9c" stroke-width="6"/><text x="41" y="50" text-anchor="middle" font-family="Jost,sans-serif" font-weight="600" font-size="24" fill="#8b4a9c">$</text></svg>
    </div>
    <h3>LOREM IPSUM CONSECTETUR</h3>
    <p>Lorem ipsum dolor sit amet consectetur adipiscing elit sed do eiusmod tempor incididunt labore et dolore magna aliqua.enim minim veniam quis nostrud exercitation.</p>
  </div>
  <div class="service" style="top:849px">
    <div class="icon" style="top:-22px">
      <svg width="82" height="82" viewBox="0 0 82 82" fill="#8b4a9c"><rect x="26" y="46" width="6" height="12"/><rect x="35" y="41" width="6" height="17"/><rect x="44" y="36" width="6" height="22"/><rect x="53" y="31" width="6" height="27"/><path d="M26 42 L44 30 L52 26" fill="none" stroke="#8b4a9c" stroke-width="3"/><path d="M48 22 L58 22 L56 31 Z"/></svg>
    </div>
    <h3>LOREM IPSUM CONSECTETUR</h3>
    <p>Lorem ipsum dolor sit amet consectetur adipiscing elit sed do eiusmod tempor incididunt labore et dolore magna aliqua.enim minim veniam quis nostrud exercitation.</p>
  </div>
  <div class="service" style="top:963px">
    <div class="icon" style="top:-22px">
      <svg width="82" height="82" viewBox="0 0 82 82"><circle cx="33" cy="50" r="8" fill="none" stroke="#8b4a9c" stroke-width="6"/><path d="M40 32 L58 52" stroke="#8b4a9c" stroke-width="6" stroke-linecap="round"/><circle cx="40" cy="30" r="6" fill="#8b4a9c"/></svg>
    </div>
    <h3>LOREM IPSUM CONSECTETUR</h3>
    <p>Lorem ipsum dolor sit amet consectetur adipiscing elit sed do eiusmod tempor incididunt labore et dolore magna aliqua.enim minim veniam quis nostrud exercitation.</p>
  </div>

  <div class="about-photo" style="left:0;width:303px" role="img" aria-label="Photo of plants growing in a greenhouse"></div>
  <div class="about-photo" style="left:898px;width:302px" role="img" aria-label="Photo of plants growing in a greenhouse"></div>
  <section class="about-panel">
    <div class="about-bracket"></div>
    <h2 class="about-title">About Us</h2>
    <div class="about-person" role="img" aria-label="Portrait photo of a team member"></div>
  </section>
</div>
</body>
</html>
```